Business Card Design Project

Professional business cards for law firm - a rough example of what we are looking for is attached. The logo, colour and styling of the name are all new and dont need to be changed. We need layout for front and back. We are looking for some imaginative layout of info. We are a young vibrant firm and not too conservative and are not adverse to something quite different.
Updates

Thank you for all the submissions.  We have been blown away with the quality of your work.  Our management team will be meeting later in the week to make our decision.  Again, thanks for the fabulous work.

Industry/Entity Type

Conservative

Requirements
Must have
• Logo and name as in attached example (colour and font)
Should not have
• Scales of Justice

```html
<!DOCTYPE html>
<html lang="en">
<head>
<meta charset="utf-8">
<title>Marlow Finch Legal – Business Cards</title>
<link rel="stylesheet" href="https://fonts.googleapis.com/css2?family=Open+Sans:ital,wght@0,400;0,600;1,400&family=Oswald:wght@700&family=Nunito+Sans:wght@400;600&display=swap">
<style>
  :root {
    --page: #ffffff;
    --card-light: #6c6c6c;
    --card-mid: #4a4a4a;
    --card-dark: #363636;
    --brand-green: #7ab648;
    --name-yellow: #f7f283;
    --text-white: #ffffff;
    --text-soft: #e6e6e6;
    --band-text: #333333;
  }
  * { margin: 0; padding: 0; box-sizing: border-box; }
  html, body {
    width: 1200px; height: 900px; overflow: hidden;
    background: var(--page);
  }
  .canvas { position: relative; width: 1200px; height: 900px; }

  .card {
    position: absolute;
    width: 570px; height: 324px;
    overflow: hidden;
  }

  /* Front */
  .card-front {
    left: 67px; top: 160px;
    background: radial-gradient(circle at 62% 52%, var(--card-light) 0%, var(--card-mid) 45%, var(--card-dark) 100%);
  }
  .brand-circle {
    position: absolute; left: 62px; top: 87px;
    width: 154px; height: 154px;
  }
  .brand-name {
    position: absolute; left: 236px; top: 128px;
    width: 280px; text-align: center;
    font-family: "Open Sans", sans-serif; font-weight: 600;
    color: var(--brand-green); line-height: 1;
  }
  .brand-name .brand-main { display: block; font-size: 42px; white-space: nowrap; }
  .brand-name .brand-sub { display: block; font-size: 22px; letter-spacing: 5px; margin-top: 4px; }
  .tagline {
    position: absolute; left: 280px; top: 204px;
    font-family: "Open Sans", sans-serif; font-style: italic;
    font-size: 12.5px; color: var(--text-soft); letter-spacing: 0.3px;
  }

  /* Back */
  .card-back {
    left: 554px; top: 366px;
    background: radial-gradient(circle at 60% 35%, var(--card-light) 0%, var(--card-mid) 45%, var(--card-dark) 100%);
    font-family: "Nunito Sans", sans-serif; color: var(--text-white);
    text-align: center;
  }
  .services {
    position: absolute; left: 0; right: 0; top: 15px;
    font-size: 15px; line-height: 20px; font-weight: 600;
  }
  .person { position: absolute; left: 0; right: 0; top: 124px; }
  .person-name {
    font-family: "Oswald", sans-serif; font-weight: 700;
    font-size: 34px; line-height: 42px; color: var(--name-yellow);
    transform: scaleX(0.95);
  }
  .person-role { font-size: 15px; letter-spacing: 4px; margin-top: -2px; }
  .contact {
    position: absolute; left: 0; right: 0; top: 217px;
    font-style: normal; line-height: 18px;
  }
  .contact .address { font-size: 16px; }
  .contact .numbers { font-size: 18px; }
  .email-band {
    position: absolute; left: 0; right: 0; top: 293px; height: 21px;
    background: var(--name-yellow); color: var(--band-text);
    font-size: 15px; line-height: 21px; font-weight: 600;
  }
</style>
</head>
<body>
<main class="canvas">

  <section class="card card-front" aria-label="Card front">
    <svg class="brand-circle" viewBox="0 0 154 154" aria-hidden="true">
      <circle cx="77" cy="77" r="74" fill="none" stroke="var(--brand-green)" stroke-width="3"/>
    </svg>
    <h1 class="brand-name">
      <span class="brand-main">Marlow Finch</span>
      <span class="brand-sub">LEGAL</span>
    </h1>
    <p class="tagline">helping you find the way forward</p>
  </section>

  <section class="card card-back" aria-label="Card back">
    <p class="services">
      Family . Restraining Orders . Probate/Wills . Dividing Fences<br>
      Traffic . Criminal . Debt Recovery . Financial Agreements
    </p>
    <div class="person">
      <h2 class="person-name">Clara Marlow LLB BA</h2>
      <p class="person-role">Solicitor</p>
    </div>
    <address class="contact">
      <div class="address">4/27 Kestrel Road, Redcliffe WA 6104</div>
      <div class="address">PO Box 512, Redcliffe WA 6984</div>
      <div class="numbers">phone: 9400 1234, 6100 5678</div>
      <div class="numbers">fax: 6300 9876</div>
    </address>
    <p class="email-band">email: reception@marlowfinchlegal.com.au</p>
  </section>

</main>
</body>
</html>
```